RB's Sports Bar Menu (Cape Cod Sports Bar)

We are a new england sports bar based on Cape Cod.

We are an old school type sports bar with pizza and wings type food.

We want to highlight our pizza as the main draw on our menu.

The style we are looking for is a placemat menu that looks casual and fun.

We want the following sections:
Starters:

Soups:

Salads:

Handhelds:

Plates:

Sides:

Desserts:

I can provide a draft of all the menu items upon request didn't want to overload this text box thank you!

• The menu must be LANDSCAPE design as it is going on a paper placemat. It also needs to all fit on ONE SIDE.

```html
<!DOCTYPE html>
<html lang="en">
<head>
<meta charset="utf-8">
<title>RB's Sports Bar Menu</title>
<link rel="stylesheet" href="https://fonts.googleapis.com/css2?family=Rye&family=Staatliches&display=swap">
<style>
  :root {
    --backdrop: #2e1c11;
    --paper-edge: #e8dcc6;
    --paper: #f5efe0;
    --navy: #2b4656;
    --brick: #952f35;
    --ink: #111111;
    --art-warm: #e4d6bd;
    --art-light: #ece3d2;
  }
  * { margin: 0; padding: 0; box-sizing: border-box; }
  html, body {
    width: 1200px;
    height: 1200px;
    overflow: hidden;
    background: var(--backdrop);
  }
  .placemat {
    position: absolute;
    left: 116px;
    top: 274px;
    width: 968px;
    height: 614px;
    background: radial-gradient(ellipse at 50% 50%, var(--paper) 60%, var(--paper-edge) 100%);
    box-shadow: 8px 10px 14px rgba(0, 0, 0, 0.45);
  }
  .frame {
    position: absolute;
    inset: 0;
    width: 968px;
    height: 614px;
  }
  .frame__outer { fill: none; stroke: var(--navy); stroke-width: 4; }
  .frame__inner { fill: none; stroke: var(--brick); stroke-width: 1.5; }

  .brand {
    position: absolute;
    left: 61px;
    top: 82px;
    width: 222px;
    text-align: center;
    font-family: "Staatliches", sans-serif;
    font-size: 34px;
    line-height: 1.1;
    letter-spacing: 1px;
    color: var(--ink);
  }
  .title {
    position: absolute;
    left: 342px;
    top: 68px;
    font-family: "Rye", serif;
    font-size: 80px;
    font-weight: 400;
    line-height: 1;
    letter-spacing: 0;
    color: var(--brick);
  }
  .art {
    position: absolute;
    border-radius: 50%;
  }
  .art--pizza {
    left: 663px;
    top: 69px;
    width: 241px;
    height: 132px;
    background: radial-gradient(ellipse at center, var(--art-warm) 0%, var(--art-light) 75%, transparent 100%);
  }
  .art--wings {
    left: 655px;
    top: 440px;
    width: 263px;
    height: 137px;
    background: radial-gradient(ellipse at center, var(--art-warm) 0%, var(--art-light) 75%, transparent 100%);
  }
  .section-head {
    position: absolute;
    width: 187px;
    height: 28px;
    border-bottom: 1.5px solid var(--ink);
    font-family: "Staatliches", sans-serif;
    font-size: 25px;
    font-weight: 400;
    line-height: 28px;
    letter-spacing: 1px;
    color: var(--ink);
  }
  .section-head--starters  { left: 60px;  top: 217px; }
  .section-head--salads    { left: 272px; top: 215px; }
  .section-head--sides     { left: 498px; top: 214px; }
  .section-head--desserts  { left: 722px; top: 249px; }
  .section-head--soups     { left: 60px;  top: 381px; }
  .section-head--handhelds { left: 272px; top: 379px; }
  .section-head--plates    { left: 497px; top: 377px; }
</style>
</head>
<body>
  <main class="placemat">
    <svg class="frame" viewBox="0 0 968 614" aria-hidden="true">
      <path class="frame__outer" d="M54 23 H914 A27 27 0 0 0 941 50 V561 A27 27 0 0 0 914 588 H54 A27 27 0 0 0 27 561 V50 A27 27 0 0 0 54 23 Z"/>
      <path class="frame__inner" d="M57 33 H911 A20 20 0 0 0 931 53 V558 A20 20 0 0 0 911 578 H57 A20 20 0 0 0 37 558 V53 A20 20 0 0 0 57 33 Z"/>
    </svg>

    <div class="brand">RB's<br>Sports Bar</div>
    <h1 class="title">MENU</h1>

    <div class="art art--pizza" role="img" aria-label="Line illustration of a pepperoni and mushroom pizza with one slice pulled out"></div>
    <div class="art art--wings" role="img" aria-label="Line illustration of a pile of chicken wings with a dipping sauce cup"></div>

    <h2 class="section-head section-head--starters">Starters:</h2>
    <h2 class="section-head section-head--salads">Salads:</h2>
    <h2 class="section-head section-head--sides">Sides:</h2>
    <h2 class="section-head section-head--desserts">Desserts:</h2>
    <h2 class="section-head section-head--soups">Soups:</h2>
    <h2 class="section-head section-head--handhelds">Handhelds:</h2>
    <h2 class="section-head section-head--plates">Plates:</h2>
  </main>
</body>
</html>
```